Website Wordpress Design

Hello all,

Real Estate Investor seeking a sleek user friendly word-press website. We are using this site to promote our real estate deals and raising capital from individuals who want to learn how to make money in real estate. The site will have 5 pages, Below you will see files explaining the site format and logo design. The website address is quietharborledger.com.***Must be able to retrieve word-press log-in username and password for future updates***

Here are some sites we like: fenwickcapitalcircle.com and seniorcarebuildworks.com

Target Market(s)

Individuals 40 and above.

Industry/Entity Type

Real Estate

Contact Information for Business Card

I'm seeking a killer business card design see details below.
Tessa Morlow
Managing Partner
RTN Estates, LLC
482 Linwood Terrace Suite 356
Brooklyn, NY 11298
Direct:917-555-0143
www.quietharborledger.com
tessa@qhledger.com

Number of Pages Required

5+ page

Font styles to use
Serif
Sans Serif

Requirements
Must have
• Good Color schemes and appealing to the eye.
Should not have
• Money symbols or images of houses

```html
<!DOCTYPE html>
<html lang="en">
<head>
<meta charset="utf-8">
<title>Quiet Harbor Ledger Explained</title>
<link rel="stylesheet" href="https://fonts.googleapis.com/css2?family=Lato:ital,wght@0,400;0,700;1,400&family=Montserrat:wght@600&display=swap">
<style>
  :root {
    --gold: #b09a55;
    --gold-text: #b7a263;
    --ink: #1a1a1a;
    --body: #222;
    --footer: #2c2c2c;
    --footer-deep: #1d1d1d;
    --rule: #9a8a55;
    --white: #fff;
  }
  * { margin: 0; padding: 0; box-sizing: border-box; }
  html, body { width: 986px; height: 1200px; overflow: hidden; }
  body { position: relative; background: var(--white); font-family: "Lato", sans-serif; color: var(--body); }

  .topbar { position: absolute; top: 0; left: 0; width: 986px; height: 42px; background: var(--gold); }
  .topbar-item { position: absolute; top: 7px; display: flex; align-items: center; gap: 9px; color: var(--white); font-weight: 700; font-size: 16px; }
  .topbar-item.phone { left: 50px; }
  .topbar-item.mail { left: 196px; }
  .icon-disc { width: 27px; height: 27px; border-radius: 50%; background: var(--white); display: flex; align-items: center; justify-content: center; }
  .menu-toggle { position: absolute; left: 910px; top: 8px; width: 27px; height: 27px; border-radius: 50%; background: var(--white); display: flex; align-items: center; justify-content: center; }

  .hero { position: absolute; top: 42px; left: 0; width: 986px; height: 241px;
    background: radial-gradient(circle at 22% 60%, #c9a64a 0 6%, #6d6252 12%, #a9a49a 32%, #cfcbc4 55%, #e4e1dc 75%, #b9b4ac 100%); }
  .hero-title { position: absolute; right: 50px; top: 74px; text-align: right; font-family: "Montserrat", sans-serif; font-weight: 600; font-size: 27px; line-height: 35px; color: #111; letter-spacing: 0.2px; white-space: nowrap; }

  .page-title { position: absolute; left: 49px; top: 307px; width: 513px; padding-bottom: 12px; border-bottom: 1px dotted #777; font-size: 29px; line-height: 36px; font-weight: 700; letter-spacing: 0.5px; color: var(--ink); white-space: nowrap; }
  .page-title .accent { color: var(--gold-text); font-weight: 400; margin-right: 4px; }

  .article { position: absolute; left: 51px; top: 370px; width: 883px; font-size: 12px; line-height: 21.6px; letter-spacing: 0.1px; }
  .article p { margin-bottom: 9px; }
  .feature-photo { float: right; width: 310px; height: 180px; margin: 2px 0 10px 20px; border: 4px solid #e3e3e3;
    background: linear-gradient(180deg, #8a8f96 0%, #c9b08a 45%, #d88f2e 62%, #6a5424 80%, #c5ab90 100%); }
  .article .cta { color: var(--gold-text); font-size: 14px; }
  .cta-line { border-bottom: 1px solid var(--rule); padding-bottom: 2px; }
  .article-end { position: absolute; left: 51px; top: 903px; width: 882px; border-top: 1px solid var(--rule); }

  .site-footer { position: absolute; top: 912px; left: 0; width: 986px; height: 240px; background: var(--footer); color: #eee; }
  .footer-col { position: absolute; top: 22px; }
  .footer-col h3 { font-weight: 400; font-size: 16px; letter-spacing: 0.4px; color: var(--white); padding-bottom: 9px; border-bottom: 1px solid #555; margin-bottom: 18px; white-space: nowrap; }
  .footer-col h3 span { color: var(--gold-text); }
  .quick-links { left: 52px; width: 133px; }
  .quick-links li { list-style: none; font-size: 11.5px; line-height: 14px; margin-bottom: 7px; padding-left: 11px; position: relative; }
  .quick-links li::before { content: "›"; position: absolute; left: 0; top: -1px; font-size: 13px; }
  .quick-links li.current { color: var(--gold-text); }
  .contact { left: 233px; width: 179px; font-size: 11.5px; line-height: 16px; }
  .contact strong { display: block; }
  .contact-row { display: flex; align-items: center; gap: 8px; margin-top: 13px; white-space: nowrap; }
  .location { left: 461px; width: 220px; }
  .map-area { width: 220px; height: 136px; border: 3px solid var(--white); background: linear-gradient(135deg, #e7e4dc, #d9d5cc); }
  .newsletter { left: 733px; width: 200px; }
  .newsletter p { font-style: italic; font-size: 11.5px; line-height: 16px; margin-bottom: 12px; }
  .email-field { width: 200px; height: 35px; border: 1px solid #ddd; border-radius: 4px; padding: 0 12px; display: flex; align-items: center; font-size: 12.5px; color: #eee; }
  .subscribe { margin: 15px 0 0 3px; width: 98px; height: 32px; background: var(--gold); color: var(--white); font-weight: 700; font-size: 12px; letter-spacing: 0.4px; display: flex; align-items: center; justify-content: center; border-radius: 2px; }

  .legal-bar { position: absolute; top: 1152px; left: 0; width: 986px; height: 48px; background: var(--footer-deep); color: #eee; }
  .copyright { position: absolute; left: 49px; top: 16px; font-size: 12px; }
  .social { position: absolute; top: 10px; left: 792px; display: flex; gap: 9px; }
  .social span { width: 29px; height: 29px; border-radius: 50%; border: 2px solid #ddd; }
</style>
</head>
<body>
  <header class="topbar">
    <div class="topbar-item phone">
      <span class="icon-disc"><svg width="14" height="14" viewBox="0 0 24 24"><path d="M6.6 10.8a15 15 0 0 0 6.6 6.6l2.2-2.2c.3-.3.7-.4 1-.2 1.1.4 2.3.6 3.6.6.6 0 1 .4 1 1V20c0 .6-.4 1-1 1A17 17 0 0 1 3 4c0-.6.4-1 1-1h3.5c.6 0 1 .4 1 1 0 1.3.2 2.5.6 3.6.1.3 0 .7-.2 1z" fill="#111"/></svg></span>
      123 456 7890
    </div>
    <div class="topbar-item mail">
      <span class="icon-disc"><svg width="14" height="11" viewBox="0 0 14 11"><rect x="0.5" y="0.5" width="13" height="10" rx="1" fill="#111"/><path d="M1 1l6 5 6-5" stroke="#fff" stroke-width="1.2" fill="none"/></svg></span>
      info@quietharborledger.com
    </div>
    <div class="menu-toggle"><svg width="13" height="9" viewBox="0 0 13 9"><rect width="13" height="1.8" fill="#111"/><rect y="3.6" width="13" height="1.8" fill="#111"/><rect y="7.2" width="13" height="1.8" fill="#111"/></svg></div>
  </header>

  <section class="hero" role="img" aria-label="Close-up of a brass compass needle over a compass rose">
    <h1 class="hero-title">WHERE CAPITAL AND<br>OPPORTUNITIES COLLABORATE</h1>
  </section>

  <h2 class="page-title"><span class="accent">QUIET</span> HARBOR LEDGER EXPLAINED</h2>

  <main class="article">
    <div class="feature-photo" role="img" aria-label="Hands framing a sunset over a field"></div>
    <p>Real Estate Investment is a necessity. From a traditional sense of basic human needs, everyone needs shelter. With real estate you can own, rent, lease, build, store, etc. There are many options.</p>
    <p>Right now is one of the best opportunities to snap up real estate investment both because of the reduced costs and because of real estate’s potential upside. Despite potential difficulties in securing borrowed funding due to current economic conditions, you are probably not going to come across another opportunity like this for a long time to come if you let it pass you by.</p>
    <p>First, the price for real estate investment on the open market has fallen since the recession that started in 2007 and which we have yet to recover from. As with every other thing sold on the open market, the movement in the price of Real Estate Investment is determined by changes in the interaction of demand for real estate and the supply of real estate. Falling demand for real estate prior to and during the recession combined with a glut of Real Estate Investment entering the open market from foreclosures combined to hammer down real estate prices. Since the economic recovery has yet to finish and the housing market remains sluggish, the prices of real estate remain at historic depths at the moment.</p>
    <p>However, because the current economic climate is more sluggish than usual, it seems reasonable to conclude that the price of real estate investment will rise again at some time in the future. Based on this assumption, if you buy real estate right now, you are likely to be able to gain in the future from the increase in the value of your real estate on the open market.</p>
    <p>Furthermore, the cost of borrowing money is unusually low at the moment due to the recession. Since most of us pay for the purchase of real estate investment using a combination of personal resources and borrowed money, this is a significant factor in the real cost of buying real estate. This is particularly true if you are able to lock in current interest rates for the near future. Although the current economy might make it difficult for you to secure loans from the usual sources, the low prices of real estate on the open market also makes it easy for you to pay a large enough down payment to sway the minds of potential lenders.</p>
    <p class="cta-line">Quiet Harbor Ledger targets mortgage notes and senior housing across the US. Each property is carefully selected following a conservative investment strategy. If you are interested in learning more, <span class="cta">Please contact Quiet Harbor Ledger today!</span></p>
  </main>
  <div class="article-end"></div>

  <footer class="site-footer">
    <nav class="footer-col quick-links">
      <h3>QUICK <span>LINKS</span></h3>
      <ul>
        <li>Home</li>
        <li class="current">Quiet Harbor Ledger Explained</li>
        <li>About Us</li>
        <li>Resources</li>
        <li>Blog</li>
        <li>Contact Us</li>
      </ul>
    </nav>
    <div class="footer-col contact">
      <h3>CONTACT <span>DETAILS</span></h3>
      <strong>QUIET HARBOR LEDGER</strong>
      53 S. Kjdurwe swrty&nbsp; 300<br>Loren ipsum , GA 30009
      <div class="contact-row"><svg width="11" height="11" viewBox="0 0 24 24"><path d="M6.6 10.8a15 15 0 0 0 6.6 6.6l2.2-2.2c.3-.3.7-.4 1-.2 1.1.4 2.3.6 3.6.6.6 0 1 .4 1 1V20c0 .6-.4 1-1 1A17 17 0 0 1 3 4c0-.6.4-1 1-1h3.5c.6 0 1 .4 1 1 0 1.3.2 2.5.6 3.6.1.3 0 .7-.2 1z" fill="#ddd"/></svg>123 456 7890</div>
      <div class="contact-row"><svg width="10" height="14" viewBox="0 0 10 14"><rect x="1" y="0.5" width="8" height="13" rx="1.5" fill="none" stroke="#ddd" stroke-width="1.3"/><circle cx="5" cy="11" r="0.9" fill="#ddd"/></svg>123 456 7890</div>
      <div class="contact-row"><svg width="12" height="9" viewBox="0 0 14 11"><rect x="0.5" y="0.5" width="13" height="10" fill="#ddd"/><path d="M1 1l6 5 6-5" stroke="#2c2c2c" stroke-width="1.2" fill="none"/></svg>info@quietharborledger.com</div>
    </div>
    <div class="footer-col location">
      <h3>LOCATION <span>MAP</span></h3>
      <div class="map-area" role="img" aria-label="Street map showing the office location"></div>
    </div>
    <div class="footer-col newsletter">
      <h3>NEWSLETTER <span>SIGN UP</span></h3>
      <p>Please Sign Up For Our Newsletter To Get All The Updates!</p>
      <div class="email-field">Email Address</div>
      <div class="subscribe">SUBSCRIBE</div>
    </div>
  </footer>

  <div class="legal-bar">
    <p class="copyright">Copyright © 2016 Quiet Harbor Ledger.&nbsp;&nbsp; All Rights Reserved.</p>
    <div class="social" aria-label="Social links"><span></span><span></span><span></span><span></span></div>
  </div>
</body>
</html>
```